Stationery - Jewellers
Business Card, Letterhead, Envelope.
I need double sided standard sized Business Card [3.5" x 2"]
Anything that looks good. Including the fonts in logo.
Professional
Imran Kazemi
Proprietor
148 Wexcombe Lane
BX4 7QT
Leeds
United Kingdom
info@corwinthegoldcrafts.co.uk
corwinthegoldcrafts.co.uk
I will welcome any ideas.
Logo and tagline: Professionals in making your loved ones smile..
Website address.
Find us on Facebook/Twitter logos.

```html
<!DOCTYPE html>
<html lang="en">
<head>
<meta charset="utf-8">
<title>Corwin The Goldcrafts – Business Card</title>
<link rel="stylesheet" href="https://fonts.googleapis.com/css2?family=Cinzel:wght@400;600&display=swap">
<style>
  :root {
    --gold: #c59a3c;
    --gold-deep: #a87a26;
    --ink: #2b2b2b;
    --emblem: #2a3038;
    --paper: #ffffff;
  }
  html, body {
    margin: 0;
    padding: 0;
    overflow: hidden;
    background: var(--paper);
  }
  .card {
    position: relative;
    width: 1200px;
    height: 686px;
    overflow: hidden;
    background: var(--paper);
    font-family: "Cinzel", "Times New Roman", serif;
  }
  .card__backdrop {
    position: absolute;
    inset: 0;
    width: 1200px;
    height: 686px;
  }
  .brand {
    position: absolute;
    left: 40px;
    top: 92px;
    width: 460px;
    margin: 0;
    color: var(--gold);
    font-weight: 600;
    text-align: center;
  }
  .brand__name {
    display: block;
    font-size: 64px;
    line-height: 1.1;
    letter-spacing: 3px;
  }
  .brand__sub {
    display: block;
    margin-top: 6px;
    font-size: 22px;
    line-height: 1.2;
    letter-spacing: 7px;
  }
  .brand__mark {
    position: absolute;
    left: 522px;
    top: 34px;
    width: 230px;
    height: 230px;
    border-radius: 50%;
    background: var(--emblem);
  }
  .contact-person {
    position: absolute;
    right: 40px;
    top: 290px;
    text-align: right;
  }
  .contact-person__name {
    margin: 0;
    color: var(--gold-deep);
    font-size: 28px;
    font-weight: 600;
    letter-spacing: 1px;
  }
  .contact-person__role {
    margin: 8px 0 0;
    color: var(--ink);
    font-size: 22px;
    font-weight: 400;
  }
  .details {
    position: absolute;
    right: 36px;
    top: 526px;
    margin: 0;
    color: var(--paper);
    font-size: 22px;
    font-style: normal;
    line-height: 34px;
    text-align: right;
    white-space: nowrap;
  }
  .details__line { margin: 0; }
  .details__label { font-weight: 600; }
</style>
</head>
<body>
<main class="card">
  <svg class="card__backdrop" viewBox="0 0 1200 686" aria-hidden="true">
    <defs>
      <linearGradient id="goldBand" x1="0" y1="0" x2="1" y2="0.4">
        <stop offset="0" stop-color="#b88a30"/>
        <stop offset="0.45" stop-color="#e9c877"/>
        <stop offset="0.7" stop-color="#d2ab55"/>
        <stop offset="1" stop-color="#b5862c"/>
      </linearGradient>
      <linearGradient id="silverSwoosh" x1="0" y1="0" x2="1" y2="0">
        <stop offset="0" stop-color="#d9d9db"/>
        <stop offset="0.5" stop-color="#a9a9ab"/>
        <stop offset="0.75" stop-color="#f2f2f3"/>
        <stop offset="1" stop-color="#9c9c9e"/>
      </linearGradient>
      <linearGradient id="paperTone" x1="0" y1="0" x2="0" y2="1">
        <stop offset="0" stop-color="#ffffff"/>
        <stop offset="1" stop-color="#f3f3f3"/>
      </linearGradient>
    </defs>
    <rect width="1200" height="686" fill="url(#paperTone)"/>
    <path d="M0 420 C300 400 420 468 700 450 C900 436 1050 400 1200 396 L1200 416 C1050 420 900 452 700 466 C420 486 300 430 0 440 Z" fill="url(#silverSwoosh)"/>
    <path d="M0 440 C300 430 420 486 700 466 C900 452 1050 420 1200 416 L1200 686 L0 686 Z" fill="url(#goldBand)"/>
  </svg>

  <h1 class="brand">
    <span class="brand__name">Corwin</span>
    <span class="brand__sub">The Goldcrafts</span>
  </h1>
  <div class="brand__mark" aria-hidden="true"></div>

  <section class="contact-person">
    <p class="contact-person__name">Imran Kazemi</p>
    <p class="contact-person__role">Proprietor</p>
  </section>

  <address class="details">
    <p class="details__line">148 Wexcombe Lane BX4 7QT Leeds United Kingdom</p>
    <p class="details__line"><span class="details__label">Phone</span> : 0113 496 0721 <span class="details__label">Fax</span> : 0113 496 0835</p>
    <p class="details__line"><span class="details__label">Email</span> : info@corwinthegoldcrafts.co.uk <span class="details__label">Web</span> : corwinthegoldcrafts.co.uk</p>
  </address>
</main>
</body>
</html>
```